VELMOR Website Design

We need a website designed for our company VELMOR. We are a luxury lifestyle club that will provide benefits and services for our members. The site should be clean & sleek, preferably using black and white (or darker colors). (example sites: brastelle.com, fovix.com)

Here is a link of a sample page I did using wix. (https://dunmerel7.pagebuildr.com/mysite) This can be used to get a general idea.

Target Market(s)

Upper Middle Class in the United States

Number of Pages Required

5+ page

Font styles to use
Sans Serif
Other font styles liked:
• Arial (or other similar fonts)

Requirements
Must have
• A clean design that is eye-catching and speaks to our company.
Nice to have
• Ideas for copy.

```html
<!DOCTYPE html>
<html lang="en">
<head>
<meta charset="utf-8">
<title>VELMOR — A Members Only Lifestyle Club</title>
<link href="https://fonts.googleapis.com/css2?family=Montserrat:wght@300;400;500;600;700&display=swap" rel="stylesheet">
<style>
:root{
  --ink:#15121b;
  --ink-soft:#1d1a24;
  --paper:#ffffff;
  --mist:#f0f0f0;
  --text-dark:#1b1b1b;
  --text-mid:#6d6d6d;
  --text-light:#c9c7cf;
  --line:#d4d4d4;
  --field:#f4f4f4;
}
*{box-sizing:border-box;margin:0;padding:0}
html,body{width:1200px;height:4369px;overflow:hidden}
body{font-family:"Montserrat",Arial,sans-serif;background:var(--ink);color:var(--text-dark);position:relative}
section,header,footer{position:absolute;left:0;width:1200px}
.abs{position:absolute}
.center{left:0;width:1200px;text-align:center}
.section-title{font-weight:400;font-size:29px;letter-spacing:.5px}
.rule{position:absolute;left:582px;width:36px;height:2px}

/* hero */
.hero{top:0;height:801px;background:radial-gradient(ellipse at 45% 40%,#8a4a36 0%,#5a2a22 35%,#2a1614 70%,#140c0d 100%)}
.hero-photo{position:absolute;inset:0}
.brand{left:108px;top:38px;color:var(--paper);font-size:40px;font-weight:400;letter-spacing:1px}
.nav{right:108px;top:55px;display:flex;gap:40px;list-style:none}
.nav li{color:var(--paper);font-size:14px}
.hero-title{top:432px;color:var(--paper);font-size:50px;font-weight:400;letter-spacing:1px}
.arrow{top:440px}

/* about */
.about{top:801px;height:656px;background:var(--ink);color:var(--paper)}
.about .section-title{top:94px}
.about-photo{left:125px;top:201px;width:458px;height:344px;background:linear-gradient(135deg,#8ea87a,#c9c2b4 45%,#6d5b4d)}
.about-copy{left:638px;top:200px;width:446px;font-size:12.5px;line-height:2;color:var(--text-light)}
.about-copy strong{display:block;color:var(--paper);font-weight:600;margin-bottom:20px}
.about-copy p{margin-bottom:24px}
.btn-line{display:inline-block;border:1.5px solid currentColor;font-size:12px;text-align:center}
.about .btn-line{position:absolute;left:638px;top:517px;width:120px;height:28px;line-height:25px;color:var(--paper)}

/* services */
.services{top:1457px;height:748px;background:var(--mist)}
.services .section-title{top:104px}
.intro{font-size:12.5px;line-height:1.9;color:var(--text-mid)}
.services .intro{top:187px}
.card-img{width:298px;height:196px}
.card-title{width:298px;text-align:center;font-weight:700;font-size:19px}
.card-text{width:298px;text-align:center;font-size:12.5px;line-height:1.6;color:var(--text-mid)}
.services .btn-line{position:absolute;left:542px;top:646px;width:116px;height:28px;line-height:25px;color:var(--text-dark)}

/* apply */
.apply{top:2205px;height:519px;background:var(--paper)}
.apply .section-title{top:80px}
.field{position:absolute;height:40px;border:1px solid var(--line);font-size:12px;color:#9a9a9a;padding:12px 14px}
.apply .btn-line{position:absolute;left:542px;top:401px;width:116px;height:30px;line-height:27px;color:var(--text-dark)}

/* experience */
.experience{top:2724px;height:670px;background:var(--ink);color:var(--paper)}
.experience .section-title{top:90px}
.experience .intro{top:166px;color:var(--text-light)}
.experience .card-text{color:var(--text-light)}

/* contact */
.contact{top:3394px;height:655px;background:var(--paper)}
.contact .section-title{top:92px}
.contact-box{left:134px;top:198px;width:929px;height:346px;border:1px solid var(--line);border-top:9px solid var(--ink);background:var(--paper)}
.contact .field{background:var(--field)}
.submit-solid{position:absolute;left:40px;width:847px;height:36px;background:var(--ink);color:var(--paper);font-size:12px;text-align:center;line-height:36px}

/* footer */
.footer{top:4049px;height:320px;background:var(--ink);color:var(--paper);text-align:center}
.footer-address{top:70px;font-size:16px}
.footer-phone{top:104px;font-size:15px;font-weight:600}
.socials{top:173px;left:549px;display:flex;gap:14px}
.socials span{width:13px;height:13px;border-radius:50%;background:var(--paper);display:block}
.copyright{top:230px;font-size:12px;color:var(--text-light)}
</style>
</head>
<body>

<header class="hero">
  <div class="hero-photo" role="img" aria-label="Friends raising glasses of wine in a warm, dim toast"></div>
  <div class="abs brand">VELMOR</div>
  <ul class="abs nav">
    <li>Home</li><li>About</li><li>Services &amp; benefits</li><li>Apply</li><li>Contact</li>
  </ul>
  <svg class="abs arrow" style="left:60px" width="26" height="46" viewBox="0 0 26 46"><polyline points="22,3 4,23 22,43" fill="none" stroke="#ffffff" stroke-width="2.5"/></svg>
  <svg class="abs arrow" style="left:1114px" width="26" height="46" viewBox="0 0 26 46"><polyline points="4,3 22,23 4,43" fill="none" stroke="#ffffff" stroke-width="2.5"/></svg>
  <h1 class="abs center hero-title">A Members Only Lifestyle Club</h1>
</header>

<section class="about">
  <h2 class="abs center section-title">About <strong>VELMOR</strong></h2>
  <div class="rule" style="top:146px;background:var(--paper)"></div>
  <div class="abs about-photo" role="img" aria-label="Guests toasting with wine at an outdoor dinner table"></div>
  <div class="abs about-copy">
    <strong>The ultimate full service lifestyle club</strong>
    <p>VELMOR was formed to bring the best services, experiences, and exclusive opportunities to our members.</p>
    <p>With everything from private member events to private jet travel, the perks of being a VELMOR member are unmatched.</p>
    <p>Professional athletes, artists, musicians, corporate professionals. Our members come from diverse backgrounds.</p>
    <p>Comprehensive services like 24/7 concierge, accountants, attorneys, private advisers, planners, investment advisors and more.</p>
  </div>
  <div class="btn-line">Apply</div>
</section>

<section class="services">
  <h2 class="abs center section-title">Services &amp; Benefits</h2>
  <div class="rule" style="top:156px;background:var(--text-dark)"></div>
  <p class="abs center intro">VELMOR membership provides you with amazing benefits and services.<br>Members receive access to the best accountants, attorneys, real estate agents, private bankers/advisers and more.<br>VELMOR members also receive access to private flight travel, premium luxury gym memberships, private social clubs, and private investment opportunities.</p>

  <div class="abs card-img" style="left:125px;top:305px;background:linear-gradient(160deg,#6f9bd8,#dfe6ee 55%,#8a1e22)" role="img" aria-label="Private jet on the tarmac with a red carpet"></div>
  <div class="abs card-img" style="left:451px;top:305px;background:linear-gradient(180deg,#c98aa6,#f3b27a 45%,#4f8fa6)" role="img" aria-label="Infinity pool at sunset"></div>
  <div class="abs card-img" style="left:783px;top:305px;background:linear-gradient(160deg,#3a2a24,#8a5432 50%,#1e1612)" role="img" aria-label="Candlelit private event dinner table"></div>

  <div class="abs card-title" style="left:125px;top:522px">Private Jet Travel</div>
  <div class="abs card-title" style="left:451px;top:522px">Experience</div>
  <div class="abs card-title" style="left:783px;top:522px">Private Events</div>
  <p class="abs card-text" style="left:125px;top:550px">Fly on your schedule with private charter access.<br>Seamless travel, anywhere you go.</p>
  <p class="abs card-text" style="left:451px;top:550px">Curated stays, resorts and getaways.<br>Unforgettable moments, planned for you.</p>
  <p class="abs card-text" style="left:783px;top:550px">Intimate dinners and exclusive gatherings.<br>Members only, every single time.</p>
  <div class="btn-line">More Service</div>
</section>

<section class="apply">
  <h2 class="abs center section-title">Apply For a Lifestyle Club</h2>
  <div class="rule" style="top:131px;background:var(--text-dark)"></div>
  <p class="abs center intro" style="top:162px">Hey - Thanks for your interest! We will begin accepting applications in 2019.<br>In the meantime, simply fill out the indication of interest below and we will be in touch once we begin accepting applications!</p>
  <div class="abs center" style="top:235px;font-size:19px">Indication of Interest</div>
  <div class="field" style="left:175px;top:315px;width:276px">Name</div>
  <div class="field" style="left:460px;top:315px;width:280px">Email</div>
  <div class="field" style="left:749px;top:315px;width:276px">Phone</div>
  <div class="btn-line">Submit</div>
</section>

<section class="experience">
  <h2 class="abs center section-title">Experience</h2>
  <div class="rule" style="top:143px;background:var(--paper)"></div>
  <p class="abs center intro">VELMOR organizes and supports a ton of private events and parties for our members.<br>Members are also provided access to exclusive venues and events from our partners.<br>Network with other members to build lasting relationships.</p>

  <div class="abs card-img" style="left:125px;top:291px;background:linear-gradient(160deg,#b9c4cc,#8a7a66 50%,#3c3a3c)" role="img" aria-label="Man relaxing on a yacht deck"></div>
  <div class="abs card-img" style="left:451px;top:291px;background:linear-gradient(180deg,#3f8fd6,#9cc8ea 55%,#2a6aa0)" role="img" aria-label="Woman in a convertible under a blue sky"></div>
  <div class="abs card-img" style="left:783px;top:291px;background:linear-gradient(160deg,#3a1f6e,#8a3bb8 50%,#1e1a5a)" role="img" aria-label="Crowd at a concert with purple stage lights"></div>

  <div class="abs card-title" style="left:125px;top:505px">Lorem Ipsum</div>
  <div class="abs card-title" style="left:451px;top:505px">Lorem Ipsum</div>
  <div class="abs card-title" style="left:783px;top:505px">Lorem Ipsum</div>
  <p class="abs card-text" style="left:125px;top:533px">Life at sea with friends and members.<br>Sail somewhere new each season.</p>
  <p class="abs card-text" style="left:451px;top:533px">Open roads and coastal drives.<br>Freedom wherever you choose to go.</p>
  <p class="abs card-text" style="left:783px;top:533px">Front row seats and backstage access.<br>Nights you will always remember.</p>
</section>

<section class="contact">
  <h2 class="abs center section-title">We're always here, drop as a line!</h2>
  <div class="rule" style="top:144px;background:var(--text-dark)"></div>
  <div class="abs contact-box">
    <div class="field" style="left:40px;top:73px;width:275px;height:36px;padding:10px 14px">Name</div>
    <div class="field" style="left:325px;top:73px;width:276px;height:36px;padding:10px 14px">Email</div>
    <div class="field" style="left:611px;top:73px;width:276px;height:36px;padding:10px 14px">Phone</div>
    <div class="field" style="left:40px;top:122px;width:847px;height:108px">Message</div>
    <div class="submit-solid" style="top:251px">Submit</div>
  </div>
</section>

<footer class="footer">
  <div class="abs center footer-address">1420 Larkspur Court, Juneau, Alaska 99801</div>
  <div class="abs center footer-phone">Phone: 1-888-555-0142</div>
  <div class="abs socials" aria-label="Social links"><span></span><span></span><span></span><span></span><span></span></div>
  <div class="abs center copyright">© 2018 Velmor All Right Reserved</div>
</footer>

</body>
</html>
```